Business Card

Please design a business card with our logo on a cream coloured background and include the following information:

Tallowmere Shopping Centre
ph (08) 9314 8806

sales@quillmeadowflorist.com

www.quillmeadowflorist.com

on reverse:

Find us on Bloomly
bloomly.com/quillmeadowflorist

```html
<!DOCTYPE html>
<html lang="en">
<head>
<meta charset="utf-8">
<title>Quill Meadow Florist – Business Card</title>
<link href="https://fonts.googleapis.com/css2?family=Ubuntu:wght@500&family=Della+Respira&display=swap" rel="stylesheet">
<style>
  :root {
    --canvas: #eeefef;
    --cream-light: #fdf6dc;
    --peach: #f8d9c4;
    --apricot: #f7d2a6;
    --ink: #464349;
    --leaf: #5b7f2c;
    --shadow: rgba(0,0,0,0.18);
  }
  * { box-sizing: border-box; margin: 0; padding: 0; }
  html, body { width: 942px; height: 1200px; overflow: hidden; }
  body { background: var(--canvas); position: relative; }

  .card {
    position: absolute;
    left: 90px;
    width: 759px;
    height: 448px;
    box-shadow: 0 14px 18px -10px var(--shadow);
    overflow: hidden;
  }
  .card--front { top: 93px; }
  .card--back { top: 609px; }

  .card__backdrop {
    position: absolute; inset: 0;
    background:
      radial-gradient(ellipse 45% 70% at 48% 20%, var(--cream-light), transparent 70%),
      linear-gradient(100deg, var(--apricot) 0%, var(--peach) 30%, var(--cream-light) 50%, var(--peach) 70%, var(--apricot) 100%);
  }

  .brand-mark {
    position: absolute;
    left: 50%;
    transform: translateX(-50%);
    width: 112px; height: 112px;
    border: 4px solid var(--leaf);
    border-radius: 50%;
  }
  .card--front .brand-mark { top: 53px; }
  .card--back .brand-mark { top: 42px; }

  .brand-name {
    position: absolute; left: 0; right: 0;
    text-align: center;
    font-family: "Ubuntu", sans-serif;
    font-weight: 500;
    color: var(--ink);
  }
  .card--front .brand-name { top: 176px; font-size: 44px; line-height: 52px; }

  .contact-list {
    position: absolute;
    left: 186px; top: 260px;
    list-style: none;
    font-family: "Della Respira", serif;
    color: var(--ink);
  }
  .contact-list li {
    display: flex; align-items: center;
    height: 38px;
    font-size: 22px;
    white-space: nowrap;
  }
  .contact-list .contact--phone { font-size: 27px; letter-spacing: 1px; }
  .contact-list .contact--phone span { padding-left: 40px; }
  .contact-icon { width: 22px; height: 22px; margin-right: 12px; flex: none; }

  .social-heading {
    position: absolute; left: 0; right: 0; top: 222px;
    text-align: center;
    font-family: "Della Respira", serif;
    font-weight: 400;
    font-size: 31px;
    line-height: 40px;
    color: var(--ink);
  }
  .social-link {
    position: absolute; left: 120px; top: 300px;
    display: flex; align-items: center;
    font-family: "Della Respira", serif;
    font-size: 26px;
    line-height: 34px;
    color: var(--ink);
    white-space: nowrap;
  }
  .social-link__square {
    width: 24px; height: 24px;
    border: 2px solid var(--ink);
    border-radius: 4px;
    margin-right: 14px;
  }
</style>
</head>
<body>

<section class="card card--front">
  <div class="card__backdrop" role="img" aria-label="Soft cream and peach background with faint translucent petal swirls"></div>
  <div class="brand-mark"></div>
  <h1 class="brand-name">Quill Meadow Florist</h1>
  <ul class="contact-list">
    <li>
      <svg class="contact-icon" viewBox="0 0 22 22" aria-hidden="true">
        <path d="M2 9 L11 3 L20 9 Z" fill="var(--leaf)"/>
        <rect x="4" y="9" width="14" height="10" fill="none" stroke="var(--leaf)" stroke-width="2"/>
        <line x1="11" y1="9" x2="11" y2="19" stroke="var(--leaf)" stroke-width="2"/>
      </svg>
      <span>Tallowmere Shopping Centre</span>
    </li>
    <li class="contact--phone">
      <svg class="contact-icon" viewBox="0 0 22 22" aria-hidden="true">
        <path d="M5 2 L9 6 L7 9 C8 12 10 14 13 15 L16 13 L20 17 L17 20 C10 19 3 12 2 5 Z" fill="var(--leaf)"/>
      </svg>
      <span>(08) 9314 8806</span>
    </li>
    <li>
      <svg class="contact-icon" viewBox="0 0 22 22" aria-hidden="true">
        <rect x="2" y="5" width="18" height="12" fill="none" stroke="var(--leaf)" stroke-width="1.8"/>
        <path d="M2 5 L11 12 L20 5" fill="none" stroke="var(--leaf)" stroke-width="1.8"/>
      </svg>
      <span>sales@quillmeadowflorist.com</span>
    </li>
    <li>
      <svg class="contact-icon" viewBox="0 0 22 22" aria-hidden="true">
        <circle cx="11" cy="11" r="9" fill="none" stroke="var(--leaf)" stroke-width="1.8"/>
        <ellipse cx="11" cy="11" rx="4" ry="9" fill="none" stroke="var(--leaf)" stroke-width="1.5"/>
        <line x1="2" y1="11" x2="20" y2="11" stroke="var(--leaf)" stroke-width="1.5"/>
      </svg>
      <span>www.quillmeadowflorist.com</span>
    </li>
  </ul>
</section>

<section class="card card--back">
  <div class="card__backdrop" role="img" aria-label="Soft cream and peach background with faint translucent petal swirls"></div>
  <div class="brand-mark"></div>
  <h2 class="social-heading">Find us on Bloomly</h2>
  <p class="social-link"><span class="social-link__square"></span>bloomly.com/quillmeadowflorist</p>
</section>

</body>
</html>
```